Create Vertical Dog Food Labels (3 inches x 5 inches) for PupKitchen

We need a packing Vertical label (3 inches x 5 inches) design for our line of Dog Food - Pup Kitchen at pupkitchenmeals.com (please review website). This design is for Custom Roll Labels. We have a logo already. Use our logo colors on label. What we need incorporated is a list of our ingredients:

50% Choice Beef
20% Pasture-raised Chicken
15% Brown Rice
15% Fresh Vegetables - Carrots, Kale, Zucchini
Herbal Health Boosters

We also need these lines at the bottom of the label:

Keeps in fridge for 4 days after thawing
Stores in freezer up to 6 months
Questions? email us at orders@meadowlanepantry.com

We have attached a sample of a competitor. The Kibble Crate.

Target Market(s)

Dog owners

Industry/Entity Type

Dog Food

Font styles to use
Sans Serif

Requirements
Must have
• Read project description above
Nice to have
• Our logo color incorporated
Should not have
• I want it simple.

```html
<!DOCTYPE html>
<html lang="en">
<head>
<meta charset="utf-8">
<title>PupKitchen – Vertical Dog Food Label 3 × 5 in</title>
<link rel="stylesheet" href="https://fonts.googleapis.com/css2?family=Montserrat:wght@400;500;600;700&display=swap">
<style>
  :root {
    --brand-green: #0b8a47;
    --herb-green: #6aa85f;
    --veg-green: #8bbf5a;
    --beef-orange: #ef7a4f;
    --chicken-yellow: #f5a623;
    --rice-peach: #f6c36a;
    --trim-pink: #e9a6d6;
    --ink: #111111;
    --paper: #ffffff;
  }
  * { box-sizing: border-box; margin: 0; padding: 0; }
  html, body { width: 1200px; height: 1000px; overflow: hidden; background: var(--paper); }
  body { position: relative; font-family: "Montserrat", Arial, sans-serif; }

  .dimension { position: absolute; color: var(--ink); font-size: 13px; }
  .dimension-width { left: 192px; top: 292px; width: 216px; text-align: center; }
  .dimension-height { left: 155px; top: 490px; transform: rotate(-90deg); transform-origin: center; width: 40px; text-align: center; }
  .dimension-lines { position: absolute; left: 0; top: 0; }

  .label {
    position: absolute; left: 192px; top: 320px; width: 216px; height: 360px;
    border: 1px solid var(--trim-pink); background: var(--paper);
  }
  .brand {
    position: absolute; left: 192px; top: 350px; width: 216px;
    display: flex; flex-direction: column; align-items: center;
  }
  .brand-dot { width: 80px; height: 80px; border-radius: 50%; background: var(--herb-green); opacity: .85; }
  .brand-name { margin-top: 4px; font-size: 28px; font-weight: 600; color: var(--brand-green); letter-spacing: -0.3px; }

  .ingredient { position: absolute; left: 183px; width: 234px; height: 18px; display: flex; }
  .ingredient-pct {
    height: 100%; color: var(--paper); font-size: 10px; font-weight: 700;
    display: flex; align-items: center; justify-content: center;
  }
  .ingredient-name {
    flex: 1; height: 100%; border: 1px dashed currentColor; border-left: none;
    font-size: 7px; display: flex; align-items: center; justify-content: center;
  }
  .beef { top: 486px; color: var(--beef-orange); }
  .beef .ingredient-pct { width: 118px; background: var(--beef-orange); }
  .chicken { top: 513px; color: var(--chicken-yellow); }
  .chicken .ingredient-pct { width: 53px; background: var(--chicken-yellow); }
  .rice { top: 539px; color: var(--rice-peach); }
  .rice .ingredient-pct { width: 42px; background: var(--rice-peach); }
  .veg { top: 565px; color: var(--veg-green); }
  .veg .ingredient-pct { width: 42px; background: var(--veg-green); }

  .band {
    position: absolute; left: 183px; width: 234px; color: var(--paper);
    font-size: 7.5px; font-weight: 500; text-align: center;
    display: flex; flex-direction: column; justify-content: center; line-height: 1.35;
  }
  .band-herbal { top: 592px; height: 18px; background: var(--herb-green); }
  .band-storage { top: 632px; height: 25px; background: var(--brand-green); }

  .contact {
    position: absolute; left: 192px; top: 664px; width: 216px; text-align: center;
    font-size: 7px; color: var(--brand-green);
  }
  .contact strong { font-weight: 700; }
</style>
</head>
<body>
  <svg class="dimension-lines" width="1200" height="1000" aria-hidden="true">
    <line x1="194" y1="312" x2="406" y2="312" stroke="#111" stroke-width="1"/>
    <polygon points="192,312 200,308 200,316" fill="#111"/>
    <polygon points="408,312 400,308 400,316" fill="#111"/>
    <line x1="184" y1="322" x2="184" y2="678" stroke="#111" stroke-width="1"/>
    <polygon points="184,320 180,328 188,328" fill="#111"/>
    <polygon points="184,680 180,672 188,672" fill="#111"/>
  </svg>
  <div class="dimension dimension-width">3 inch</div>
  <div class="dimension dimension-height">5 inch</div>

  <div class="label"></div>

  <div class="brand">
    <div class="brand-dot"></div>
    <div class="brand-name">PupKitchen</div>
  </div>

  <div class="ingredient beef"><div class="ingredient-pct">50%</div><div class="ingredient-name">Choice Beef</div></div>
  <div class="ingredient chicken"><div class="ingredient-pct">20%</div><div class="ingredient-name">Pasture-raised Chicken</div></div>
  <div class="ingredient rice"><div class="ingredient-pct">15%</div><div class="ingredient-name">15% Brown Rice</div></div>
  <div class="ingredient veg"><div class="ingredient-pct">15%</div><div class="ingredient-name">15% Fresh Vegetables - Carrots, Kale, Zucchini</div></div>

  <div class="band band-herbal">Herbal Health Boosters</div>
  <div class="band band-storage">
    <span>Keeps in fridge for 4 days after thawing</span>
    <span>Stores in freezer up to 6 months</span>
  </div>

  <p class="contact"><strong>Questions?</strong> email us at orders@meadowlanepantry.com</p>
</body>
</html>
```